Halvern Cards

Technical services company
Networking, EAS, access control, project management and consultation

Clean, bold, modern design Using existing company logo for colors

Include Facebook and twitter links, QR bar code?

Industry/Entity Type

It Company

Contact Information for Business Card

Halvern Technical Services
"Steadfastly devoted to your progress"
860-555-0147 Main

Derek Voslund
Managing Partner / President
derek.voslund@halvern-ts.example
860-555-0183 Direct
www.halvern-ts.example

```html
<!DOCTYPE html>
<html lang="en">
<head>
<meta charset="utf-8">
<title>Halvern Technical Services – Business Card</title>
<link href="https://fonts.googleapis.com/css2?family=Questrial&display=swap" rel="stylesheet">
<style>
  :root {
    --backdrop: #e9ebee;
    --card-white: #ffffff;
    --brand-blue: #2a3f9c;
    --deep-blue: #1c2f8c;
    --bright-blue: #0aa9ea;
    --swoosh-green: #3dae3f;
    --ink: #222428;
    --on-blue: #ffffff;
  }
  * { margin: 0; padding: 0; box-sizing: border-box; }
  html, body {
    width: 1200px; height: 901px; overflow: hidden;
    background: var(--backdrop);
    font-family: "Questrial", "Century Gothic", sans-serif;
  }
  .business-card {
    position: absolute; left: 150px; top: 193px;
    width: 900px; height: 514px;
    border-radius: 40px; overflow: hidden;
    background: var(--card-white);
    box-shadow: 0 14px 34px rgba(0,0,0,.18);
  }
  .card-art { position: absolute; inset: 0; }
  .brand {
    position: absolute; left: 150px; top: 52px;
    display: flex; align-items: center; gap: 26px;
  }
  .brand-dot {
    width: 116px; height: 116px; border-radius: 50%;
    background: var(--brand-blue);
  }
  .brand-name {
    color: var(--brand-blue); font-size: 38px; line-height: 1.1;
  }
  .holder-name {
    position: absolute; left: 118px; top: 252px;
    font-size: 27px; letter-spacing: 2px; color: var(--ink);
  }
  .holder-title {
    position: absolute; left: 132px; top: 290px;
    font-size: 19px; color: var(--brand-blue);
  }
  .contact {
    position: absolute; right: 36px; top: 296px;
    color: var(--on-blue); text-align: right; font-size: 17px;
    list-style: none;
  }
  .contact li { display: flex; justify-content: flex-end; align-items: center; gap: 10px; height: 27px; }
  .contact .address { display: block; height: auto; line-height: 24px; margin-bottom: 10px; }
  .contact svg { width: 17px; height: 17px; flex: none; }
</style>
</head>
<body>
  <div class="business-card">
    <svg class="card-art" viewBox="0 0 900 514" aria-hidden="true">
      <defs>
        <radialGradient id="band-glow" cx="0.5" cy="0.75" r="0.6">
          <stop offset="0" stop-color="var(--bright-blue)"/>
          <stop offset="1" stop-color="var(--deep-blue)"/>
        </radialGradient>
      </defs>
      <path class="green-swoosh" d="M0,250 C90,330 250,402 440,400 L440,514 L0,514 Z" fill="var(--swoosh-green)"/>
      <path class="blue-band" d="M0,318 C120,372 270,418 430,404 C560,390 680,230 900,170 L900,514 L0,514 Z" fill="url(#band-glow)"/>
      <path class="accent-line" d="M470,382 C600,352 690,196 900,146" fill="none" stroke="var(--brand-blue)" stroke-width="3"/>
    </svg>

    <div class="brand">
      <div class="brand-dot"></div>
      <div class="brand-name">Halvern<br>Technical Services</div>
    </div>

    <div class="holder-name">DEREK VOSLUND</div>
    <div class="holder-title">Managing Partner / President</div>

    <ul class="contact">
      <li class="address">21 Orchard Row, Suite 4<br>Brookfield CT</li>
      <li>860-555-0147
        <svg viewBox="0 0 24 24"><path fill="currentColor" d="M6.6 10.8a15 15 0 0 0 6.6 6.6l2.2-2.2c.3-.3.7-.4 1-.2 1.1.4 2.3.6 3.6.6.6 0 1 .4 1 1V20c0 .6-.4 1-1 1A17 17 0 0 1 3 4c0-.6.4-1 1-1h3.5c.6 0 1 .4 1 1 0 1.3.2 2.5.6 3.6.1.3 0 .7-.2 1z"/></svg></li>
      <li>860-555-0183
        <svg viewBox="0 0 24 24"><rect x="6" y="2" width="12" height="20" rx="2" fill="none" stroke="currentColor" stroke-width="2"/><circle cx="12" cy="18" r="1.2" fill="currentColor"/></svg></li>
      <li>860-555-0192
        <svg viewBox="0 0 24 24"><rect x="3" y="9" width="18" height="12" rx="1.5" fill="currentColor"/><rect x="7" y="3" width="10" height="7" fill="none" stroke="currentColor" stroke-width="2"/></svg></li>
      <li>derek.voslund@halvern-ts.example
        <svg viewBox="0 0 24 24"><rect x="2" y="5" width="20" height="14" rx="1.5" fill="currentColor"/><path d="M3 6l9 7 9-7" fill="none" stroke="var(--deep-blue)" stroke-width="1.6"/></svg></li>
      <li>www.halvern-ts.example
        <svg viewBox="0 0 24 24"><g fill="none" stroke="currentColor" stroke-width="1.6"><circle cx="12" cy="12" r="9.5"/><ellipse cx="12" cy="12" rx="4.5" ry="9.5"/><path d="M2.5 12h19M4 7h16M4 17h16"/></g></svg></li>
    </ul>
  </div>
</body>
</html>
```